business card design for a small scale specialty cut flower farm

We need a business card design for Hollowmere Bloom Farm based in Langley, BC, Canada. We produce specialty, high-end cut flowers and sell locally to florists, local shops and markets and the end user through bouquet subscriptions. The final business card design should be memorable and have a timeless or vintage feel. We would prefer a square shape.
Updates

Target Market(s)

florists, shops and seasonal markets, local flower lovers

Industry/Entity Type

Floral

Contact Information for Business Card

Tamsin Ellery Voss, Grower
Langley, BC, Canada
website: hollowmerebloomfarm.example
instagram: @hollowmerebloomfarm
Tel: 555.317.4290
facebook: www.facebook.example/hollowmereblooms/

Font styles to use
Serif
Decorative
Script

Requirements
Must have
• soft black background colour on front side, the included logo and catch phrase: Fresh Local Seasonal
Nice to have
• phone number and website address on front of card, included photo 6539 incorporated onto the back, possibly photo 6609 as well.

```html
<!DOCTYPE html>
<html lang="en">
<head>
<meta charset="utf-8">
<title>Hollowmere Bloom Farm – Business Card</title>
<link rel="stylesheet" href="https://fonts.googleapis.com/css2?family=Delius&family=Lato:wght@400&display=swap">
<style>
  :root {
    --backdrop: #e3e3e3;
    --card: #f4f4f4;
    --card-dark: #2a2a2a;
    --ink: #1f1f1f;
    --ink-light: #f2f0ee;
    --rose: #d97fb0;
    --rose-deep: #cf6fa3;
    --blush: #f2c4bf;
    --peach: #f5d3b8;
  }
  * { box-sizing: border-box; margin: 0; padding: 0; }
  html, body { width: 1200px; height: 960px; overflow: hidden; }
  body { background: var(--backdrop); position: relative; font-family: "Lato", sans-serif; color: var(--ink); }

  .card { position: absolute; top: 246px; width: 450px; height: 446px; overflow: hidden; }
  .card--front { left: 127px; background: var(--card-dark); color: var(--ink-light); }
  .card--back { left: 631px; background: var(--card); }

  /* Front */
  .brand-dot { position: absolute; left: 180px; top: 74px; width: 90px; height: 90px; border-radius: 50%; background: var(--blush); }
  .brand-name { position: absolute; left: 0; right: 0; top: 180px; text-align: center; font-family: "Lato", sans-serif; font-weight: 400; color: var(--ink-light); }
  .brand-name__line1 { display: block; font-size: 54px; line-height: 1; letter-spacing: 1px; }
  .brand-name__line2 { display: block; font-size: 28px; line-height: 1; letter-spacing: 5px; margin-top: 14px; text-transform: uppercase; }
  .catchphrase { position: absolute; left: 0; right: 0; top: 380px; text-align: center; font-family: "Delius", cursive; font-size: 26px; color: var(--rose); }

  /* Back */
  .back-art { position: absolute; inset: 0; }
  .contact { position: absolute; left: 0; right: 0; top: 144px; text-align: center; padding-left: 20px; }
  .contact__name { font-family: "Delius", cursive; font-size: 26px; font-weight: 400; color: var(--rose); line-height: 1; }
  .contact__role { font-size: 16px; letter-spacing: 0.5px; margin-top: 8px; text-transform: uppercase; }
  .contact__icons { display: flex; justify-content: center; gap: 11px; margin-top: 22px; height: 22px; }
  .contact__icons svg { width: 22px; height: 22px; }
  .contact__lines { margin-top: 6px; font-size: 16px; line-height: 21px; letter-spacing: 0.3px; }
</style>
</head>
<body>

<section class="card card--front" aria-label="Card front">
  <div class="brand-dot" aria-hidden="true"></div>
  <h1 class="brand-name">
    <span class="brand-name__line1">Hollowmere</span>
    <span class="brand-name__line2">Bloom Farm</span>
  </h1>
  <p class="catchphrase">Fresh Local Seasonal</p>
</section>

<section class="card card--back" aria-label="Card back">
  <svg class="back-art" viewBox="0 0 450 446" width="450" height="446" aria-hidden="true">
    <defs>
      <linearGradient id="ring" x1="0" y1="0" x2="1" y2="1">
        <stop offset="0" stop-color="#f0b99a"/>
        <stop offset="1" stop-color="#d46fa6"/>
      </linearGradient>
      <radialGradient id="bloomTop" cx="0.4" cy="0.45" r="0.6">
        <stop offset="0" stop-color="#f7c8c0"/>
        <stop offset="0.7" stop-color="#f1b2ad"/>
        <stop offset="1" stop-color="#c9cdbb" stop-opacity="0"/>
      </radialGradient>
      <radialGradient id="bloomBottom" cx="0.6" cy="0.6" r="0.6">
        <stop offset="0" stop-color="#f6d6c4"/>
        <stop offset="0.6" stop-color="#f2bdb8"/>
        <stop offset="1" stop-color="#d9a39a" stop-opacity="0"/>
      </radialGradient>
    </defs>
    <g fill="none" stroke="url(#ring)">
      <ellipse cx="222" cy="222" rx="188" ry="190" stroke-width="1.2"/>
      <ellipse cx="216" cy="230" rx="180" ry="186" stroke-width="2.4" transform="rotate(-8 216 230)"/>
      <ellipse cx="228" cy="216" rx="184" ry="178" stroke-width="1"/>
    </g>
    <g role="img" aria-label="Watercolour roses, carnation and sage leaves">
      <ellipse cx="78" cy="70" rx="110" ry="100" fill="url(#bloomTop)"/>
    </g>
    <g role="img" aria-label="Watercolour cream and blush roses with dusty foliage">
      <ellipse cx="385" cy="370" rx="150" ry="160" fill="url(#bloomBottom)"/>
    </g>
  </svg>

  <div class="contact">
    <h2 class="contact__name">Tamsin Ellery Voss</h2>
    <p class="contact__role">Grower</p>
    <div class="contact__icons" aria-hidden="true">
      <svg viewBox="0 0 24 24"><path fill="var(--rose-deep)" d="M6.6 2.5l3 3.4-1.9 2.6c1.2 2.6 3.2 4.6 5.8 5.8l2.6-1.9 3.4 3-1.6 3.8C10.8 19.6 4.4 13.2 3 5.1z"/></svg>
      <svg viewBox="0 0 24 24" fill="none" stroke="var(--rose-deep)" stroke-width="1.8"><circle cx="12" cy="12" r="9"/><ellipse cx="12" cy="12" rx="4" ry="9"/><path d="M3 12h18M4.5 7.5h15M4.5 16.5h15"/></svg>
      <svg viewBox="0 0 24 24"><rect x="3" y="3" width="18" height="18" rx="4" fill="none" stroke="var(--rose-deep)" stroke-width="2.2"/></svg>
      <svg viewBox="0 0 24 24"><rect x="3" y="3" width="18" height="18" rx="2" fill="var(--rose-deep)"/></svg>
    </div>
    <div class="contact__lines">
      <p>(555) 317-4290</p>
      <p>hollowmerebloomfarm.example</p>
      <p>@hollowmerebloomfarm</p>
      <p>/hollowmereblooms</p>
    </div>
  </div>
</section>

</body>
</html>
```